Tessel PR (young, fun PR agency) needs a Business Card Design

We need a new business card design that reflects who we are as a company. We're a Sydney-based PR agency that's six years old with clients including Blue Heron, Duneprint, OLVEN, Lou Carvell etc. - just check out our website for more info: www.tesselpr.com.au. We would like to see designs that bring to life our company name and what we do (generating media coverage for brands on TV, radio, online and in newspapers and magazines). We don't want a corporate style card but one that people take notice of and think 'wow that's a cool business card'. It doesn't have to be the standard rectangle shape and can incorporate humour.

Target Market(s)

Clients (generally cool/creative types) and media

Industry/Entity Type

Business

Requirements
Must have
• The card must feature our business logo (which can be updated if you like) and use both sides.
Nice to have
• The card could feature a cool illustration

```html
<!DOCTYPE html>
<html lang="en">
<head>
<meta charset="utf-8">
<title>Tessel PR — Business Card</title>
<link href="https://fonts.googleapis.com/css2?family=Oswald:wght@700&family=Open+Sans:wght@400;700&display=swap" rel="stylesheet">
<style>
  :root {
    --page: #e9e6e1;
    --white: #ffffff;
    --orange: #f7941d;
    --orange-light: #fbb04c;
    --orange-deep: #f08a12;
    --ink: #1d1d1b;
    --ink-soft: #4a3a28;
    --text-light: #ffffff;
  }
  * { box-sizing: border-box; margin: 0; padding: 0; }
  html, body { width: 1200px; height: 900px; overflow: hidden; }
  body {
    background: var(--page);
    font-family: "Open Sans", Arial, sans-serif;
    position: relative;
  }
  .card {
    position: absolute;
    top: 282px;
    width: 543px;
    height: 310px;
    border-radius: 16px;
    overflow: hidden;
    box-shadow: 0 6px 18px rgba(0,0,0,0.18);
  }
  .card--front { left: 34px; background: var(--white); }
  .card--back {
    left: 624px;
    background: radial-gradient(circle at 50% 45%, var(--orange-light), var(--orange) 55%, var(--orange-deep));
  }
  .card__bands { position: absolute; inset: 0; width: 543px; height: 310px; }
  .band--orange { fill: var(--orange); }
  .band--white { fill: var(--white); }

  .wordmark, .tagline, .website {
    position: absolute;
    white-space: nowrap;
    transform-origin: left bottom;
  }
  .wordmark {
    font-family: "Oswald", "Arial Narrow", sans-serif;
    font-weight: 700;
    font-size: 48px;
    color: var(--ink);
    letter-spacing: 0.5px;
    line-height: 1;
    text-transform: uppercase;
  }
  .tagline {
    font-weight: 700;
    font-size: 14px;
    line-height: 1;
    color: var(--ink);
    letter-spacing: 0.3px;
  }
  .mark-circle {
    position: absolute;
    width: 104px;
    height: 104px;
    border: 4px solid var(--ink);
    border-radius: 50%;
  }

  .card--front .wordmark { left: 64px; top: 76px; transform: rotate(-3.5deg); }
  .card--front .tagline { left: 72px; top: 136px; transform: rotate(-3.5deg); }
  .card--front .mark-circle { left: 359px; top: 24px; }

  .card--back .wordmark { left: 84px; top: 134px; transform: rotate(-4.8deg); }
  .card--back .tagline { left: 94px; top: 192px; transform: rotate(-4.8deg); }
  .card--back .mark-circle { left: 374px; top: 66px; }
  .website {
    left: 116px;
    top: 218px;
    font-size: 14px;
    line-height: 1;
    letter-spacing: 2.4px;
    color: var(--ink-soft);
    transform: rotate(-4.8deg);
  }

  .person { position: absolute; left: 36px; top: 222px; color: var(--text-light); }
  .person__name { font-weight: 700; font-size: 19px; line-height: 1.25; }
  .person__email { font-size: 14px; line-height: 1.3; }

  .contact {
    position: absolute;
    left: 330px;
    top: 184px;
    font-size: 12px;
    line-height: 1.35;
    color: var(--ink-soft);
  }
  .contact__line { display: flex; align-items: center; gap: 6px; }
  .contact__line svg { width: 12px; height: 12px; fill: var(--ink); }
  .contact__address { margin-top: 20px; }
</style>
</head>
<body>
  <section class="card card--front" aria-label="Card front">
    <svg class="card__bands" viewBox="0 0 543 310" aria-hidden="true">
      <polygon class="band--orange" points="0,180 543,144 543,310 0,310"/>
      <polygon class="band--orange" points="58,130 420,108 420,132 58,154"/>
    </svg>
    <div class="wordmark">Tessel PR</div>
    <div class="mark-circle"></div>
    <div class="tagline">PUBLIC RELATIONS</div>

    <div class="person">
      <p class="person__name">Nadia Rowe</p>
      <p class="person__email">nadia@tesselpr.com.au</p>
    </div>

    <div class="contact">
      <p class="contact__line">
        <svg viewBox="0 0 12 12" aria-hidden="true"><rect x="3" y="0" width="6" height="12" rx="1.2"/></svg>
        + 61 (0)2 5550 1842
      </p>
      <p class="contact__line">
        <svg viewBox="0 0 12 12" aria-hidden="true"><path d="M1 4 Q6 0 11 4 L9.5 5.5 L8 4.5 L4 4.5 L2.5 5.5 Z M3 6 H9 L10 11 H2 Z"/></svg>
        + 61 (0)2 5550 1843
      </p>
      <p class="contact__address">Unit 3<br>48 Larkin Street<br>Harbourview NSW 2031</p>
    </div>
  </section>

  <section class="card card--back" aria-label="Card back">
    <svg class="card__bands" viewBox="0 0 543 310" aria-hidden="true">
      <polygon class="band--white" points="0,196 543,150 543,172 0,218"/>
    </svg>
    <div class="wordmark">Tessel PR</div>
    <div class="mark-circle"></div>
    <div class="tagline">PUBLIC RELATIONS</div>
    <div class="website">www.tesselpr.com.au</div>
  </section>
</body>
</html>
```